Kessler MD Summit Primary Care Business Card

Need a business card for a medical clinic targeting VIP patients. Should portray an upscale feeling. Simple, clean design. Logo and colors need to be incorporated into card. Clinic colors are gray/ silver, blues, white same as logo.
Clinic is a cash only VIP service clinic targeting higher income patients.
Tagline: "Where everyone is a VIP - Very Important Patient"

Target Market(s)

VIP, upscale

Industry/Entity Type

Medical

Contact Information for Business Card

Would like to use for cards with raised print or metallic highlight.

Requirements
Must have
• Incorporate logo, Use colors in logo
Nice to have
• Metallic detail
Should not have
• too much details or colors, other stock photos or designs

```html
<!DOCTYPE html>
<html lang="en">
<head>
<meta charset="utf-8">
<title>Kessler MD Summit Primary Care – Business Card</title>
<link href="https://fonts.googleapis.com/css2?family=Cinzel:wght@400;700&family=Open+Sans:wght@400&display=swap" rel="stylesheet">
<style>
  :root {
    --page-bg: #e9e8e5;
    --card-blue: #3c5068;
    --card-white: #f7f7f6;
    --navy: #2f4258;
    --slate: #5b6b7d;
    --silver: #b9bdc2;
    --silver-light: #dfe2e6;
    --text-gray: #6d7680;
    --white: #ffffff;
  }
  * { margin: 0; padding: 0; box-sizing: border-box; }
  html, body {
    width: 1200px; height: 900px; overflow: hidden;
    background: var(--page-bg);
  }
  .canvas {
    position: relative; width: 1200px; height: 900px;
  }
  .card {
    position: absolute; left: 300px; width: 600px; height: 340px;
    border-radius: 22px;
    box-shadow: 0 6px 18px rgba(0,0,0,0.18);
    overflow: hidden;
  }
  /* Back side */
  .card-back { top: 60px; background: var(--card-blue); }
  .back-brand {
    position: absolute; top: 110px; left: 0; width: 100%;
    text-align: center;
    font-family: 'Cinzel', serif; font-weight: 400;
    font-size: 40px; letter-spacing: 3px; color: var(--silver-light);
  }
  .tagline {
    position: absolute; left: 34px; bottom: 34px;
    font-family: 'Open Sans', sans-serif; font-size: 15px;
    color: var(--white); letter-spacing: 0.2px;
  }
  /* Front side */
  .card-front { top: 480px; background: var(--card-white); }
  .brand-block {
    position: absolute; top: 26px; left: 40px; width: 230px;
    text-align: center;
  }
  .brand-dot {
    display: block; width: 34px; height: 34px; margin: 0 auto 10px;
    border-radius: 50%; background: var(--navy);
  }
  .brand-name {
    font-family: 'Cinzel', serif; font-weight: 400;
    color: var(--navy); font-size: 15px; line-height: 1.35; letter-spacing: 1px;
  }
  .holder {
    position: absolute; top: 132px; left: 40px;
    font-family: 'Cinzel', serif;
  }
  .holder-name { font-size: 24px; color: var(--navy); letter-spacing: 1px; }
  .holder-title { font-size: 15px; color: var(--text-gray); margin-top: 2px; letter-spacing: 1px; }
  .contact {
    list-style: none; margin-top: 12px;
    font-family: 'Cinzel', serif; font-size: 13px; color: var(--slate);
    line-height: 1.6; letter-spacing: 0.5px;
  }
  .contact li { display: flex; align-items: center; gap: 7px; }
  .contact .no-icon { padding-left: 0; }
  .contact svg { width: 12px; height: 12px; flex: none; }
  .front-brand-mark {
    position: absolute; top: 110px; right: 40px; width: 260px;
    text-align: center;
    font-family: 'Cinzel', serif; font-weight: 400;
    font-size: 44px; line-height: 1.1; letter-spacing: 2px; color: var(--silver);
  }
</style>
</head>
<body>
<main class="canvas">
  <section class="card card-back" aria-label="Card back">
    <div class="back-brand">Kessler MD</div>
    <p class="tagline">Where everyone is a VIP - Very Important Patient</p>
  </section>

  <section class="card card-front" aria-label="Card front">
    <div class="brand-block">
      <span class="brand-dot" aria-hidden="true"></span>
      <div class="brand-name">KESSLER MD<br>SUMMIT PRIMARY CARE</div>
    </div>

    <div class="holder">
      <div class="holder-name">Daniel Hartwell</div>
      <div class="holder-title">CEO/Founder</div>
      <ul class="contact">
        <li class="no-icon">4120 Cedar Ridge Road</li>
        <li class="no-icon">Juneau, Alaska 34812</li>
        <li>
          <svg viewBox="0 0 24 24" aria-hidden="true"><path fill="#2f4258" d="M6.6 10.8a15.1 15.1 0 0 0 6.6 6.6l2.2-2.2a1 1 0 0 1 1-.25 11.4 11.4 0 0 0 3.6.57 1 1 0 0 1 1 1V20a1 1 0 0 1-1 1A17 17 0 0 1 3 4a1 1 0 0 1 1-1h3.5a1 1 0 0 1 1 1c0 1.25.2 2.45.57 3.57a1 1 0 0 1-.25 1z"/></svg>
          689 555 0147
        </li>
        <li>
          <svg viewBox="0 0 24 24" aria-hidden="true"><rect x="2" y="5" width="20" height="14" rx="2" fill="#2f4258"/><path d="M3 6l9 7 9-7" fill="none" stroke="#f7f7f6" stroke-width="1.8"/></svg>
          hello@kesslermd.com
        </li>
        <li class="no-icon">www.kesslermd.com</li>
      </ul>
    </div>

    <div class="front-brand-mark">Kessler<br>MD</div>
  </section>
</main>
</body>
</html>
```